Business Card Design

Electronic Security Installation Specialists

Check out our website at www.bramblecoastllc.com to see what we do.

Industry/Entity Type

Business

Contact Information for Business Card

Fern Ridge
Marisol Penton
318 Calloway Drive
Larkfield, OR 97310

Colors
3176b5
0455a3
ffffff

```html
<!DOCTYPE html>
<html lang="en">
<head>
<meta charset="utf-8">
<title>Fern Ridge – Business Card</title>
<link href="https://fonts.googleapis.com/css2?family=Cabin:wght@400;500;600&display=swap" rel="stylesheet">
<style>
  :root {
    --page: #e4e4e4;
    --brand-blue: #3176b5;
    --deep-blue: #0455a3;
    --navy: #1d3f72;
    --card-front-top: #1a4a89;
    --card-front-bottom: #122f5c;
    --white: #ffffff;
    --mark-tint: #f1f3f6;
  }
  * { margin: 0; padding: 0; box-sizing: border-box; }
  html, body {
    width: 1200px; height: 1000px; overflow: hidden;
    background: var(--page);
    font-family: "Cabin", sans-serif;
  }
  .canvas { position: relative; width: 1200px; height: 1000px; }

  .card { position: absolute; width: 805px; height: 470px; }

  .card-front {
    left: 315px; top: 57px;
    background: linear-gradient(180deg, var(--card-front-top) 0%, var(--card-front-top) 55%, var(--card-front-bottom) 100%);
    border-radius: 30px 0 30px 0;
    display: flex; align-items: center; justify-content: center;
  }
  .front-name {
    color: var(--white);
    font-size: 84px; font-weight: 500; letter-spacing: 2px;
  }

  .card-back {
    left: 72px; top: 462px;
    background: var(--white);
    border-radius: 0 0 0 30px;
    overflow: hidden;
  }
  .brand-row {
    position: absolute; left: 108px; top: 78px;
    display: flex; align-items: center; gap: 22px;
  }
  .brand-dot {
    width: 82px; height: 82px; border-radius: 50%;
    background: var(--deep-blue);
  }
  .brand-name {
    color: var(--navy);
    font-size: 56px; font-weight: 500; letter-spacing: 1px;
  }
  .faint-circle {
    position: absolute; left: -20px; top: 190px;
    width: 360px; height: 360px; border-radius: 50%;
    background: var(--mark-tint);
  }
  .contact {
    position: absolute; right: 54px; top: 298px;
    text-align: right; color: var(--navy);
  }
  .contact-name {
    color: var(--brand-blue);
    font-size: 31px; font-weight: 600; margin-bottom: 16px;
  }
  .contact-line {
    font-size: 21px; line-height: 23px;
    display: flex; justify-content: flex-end; align-items: center; gap: 9px;
  }
  .contact-line svg { fill: var(--navy); flex: none; }
</style>
</head>
<body>
<div class="canvas">

  <section class="card card-front">
    <span class="front-name">Fern Ridge</span>
  </section>

  <section class="card card-back">
    <div class="faint-circle"></div>
    <div class="brand-row">
      <span class="brand-dot"></span>
      <span class="brand-name">FERN RIDGE</span>
    </div>
    <div class="contact">
      <p class="contact-name">Marisol Penton</p>
      <p class="contact-line">
        <svg width="26" height="16" viewBox="0 0 26 16" aria-hidden="true">
          <path d="M1 6 C4 1 22 1 25 6 L22 8 L19 5 L7 5 L4 8 Z"/>
          <rect x="6" y="7" width="14" height="8" rx="2"/>
        </svg>
        <span>0000 000 0000</span>
      </p>
      <p class="contact-line">
        <svg width="12" height="18" viewBox="0 0 12 18" aria-hidden="true">
          <path d="M6 0 A6 6 0 0 1 12 6 C12 10 6 18 6 18 C6 18 0 10 0 6 A6 6 0 0 1 6 0 Z M6 3.5 A2.5 2.5 0 1 0 6 8.5 A2.5 2.5 0 1 0 6 3.5 Z"/>
        </svg>
        <span>318 Calloway Drive Larkfield,</span>
      </p>
      <p class="contact-line"><span>OR 97310</span></p>
    </div>
  </section>

</div>
</body>
</html>
```